Design a calming beauty medical salon & spa website based in Hong Kong

We need help building an informational website for a beauty salon in Hong Kong. The local salon provides facials, massages, body and other slimming treatments in a relaxing environment. We offer some non-invasive medical treatments, such as botox. Having built the business on word of mouth, it is now time for us to launch a website to help market the business better. Website requirements:

-Must be responsive
-Use vibrant but clean colours. not too many, 1-2 colours
-Must be bilingual (switch between Chinese traditional and English)
-Our current website is host on a server, not using any particular platforms like wordpress

Pages:
1/ Homepage
2/ About us (incorporate gallery of salon photos and history of company)
3/ Promotions and latest deals (and leads them to sign up for more info, maybe pop-up small window when you click on a promotion)
4/ Treatment menus
4.1/Body treatments
4.2/ Face treatments
4.3/ Slimming treatments
5/ Showcasing products sold (no e-commerce functionality, just showing off products)
6/ Contact us (tel, address, map, opening hrs)

Footer - must haves include contact us info, privacy policy, terms & conditions, copyright blurb, join our company/employment page (with a form)

For information (comparable websites we like):
http://vostaria.com/
http://quimbel.com.hk/tc/aboutquimbel/background.php#centerenvi
Attaching a very first draft concept for this website
Attaching pictures of the beauty salon
Attaching logo

Target Market(s)

Hong Kong based, Chinese, females, 30-50+ age. 90% female clients.

Industry/Entity Type

Beauty Salon

Number of Pages Required

5+ page

Font styles to use
Sans Serif

Colors
f9d9e8
fbd3d4
fee3d5
fbe7d2
fee18a
fbf289
ffffff

Requirements
Must have
• interactive elements on website, such as scrolling banner photo headers
• incorporate photos of website salon
• connect to facebook page

```html
<!DOCTYPE html>
<html lang="en">
<head>
<meta charset="utf-8">
<title>Serene Beauty</title>
<link href="https://fonts.googleapis.com/css2?family=Open+Sans:wght@400;600;700&display=swap" rel="stylesheet">
<style>
:root{
  --plum:#7a3b78;
  --plum-dark:#5e2a5c;
  --ink:#3b3b3b;
  --white:#ffffff;
  --blush:#f9d3d6;
  --peach:#fde9e2;
  --sand:#f1e4da;
  --footer:#2f2f2f;
  --hero-a:#b78a86;
  --hero-b:#d9b3ad;
}
*{margin:0;padding:0;box-sizing:border-box}
html,body{width:1200px;height:2844px;overflow:hidden}
body{font-family:"Open Sans",Arial,sans-serif;color:var(--ink);background:var(--white);position:relative}
.section-title{font-size:34px;font-weight:600;color:var(--plum);letter-spacing:1px}
.btn{display:inline-block;border:3px solid var(--plum);color:var(--plum);font-size:22px;font-weight:600;padding:10px 16px;background:transparent;letter-spacing:1px}

.site-header{position:absolute;top:0;left:0;width:1200px;height:100px;background:var(--white);display:flex;align-items:center;justify-content:space-between;padding:0 60px 0 84px}
.brand{font-size:30px;font-weight:600;color:var(--plum);display:flex;align-items:center;gap:12px}
.brand-dot{width:22px;height:22px;border-radius:50%;background:var(--plum)}
.main-nav{display:flex;gap:34px;font-size:17px;color:#666;letter-spacing:.5px}

.hero{position:absolute;top:100px;left:0;width:1200px;height:600px;background:linear-gradient(100deg,var(--hero-a) 0%,#c79d97 55%,var(--hero-b) 100%)}
.hero-photo{position:absolute;inset:0}
.hero-copy{position:absolute;left:84px;top:148px;width:700px;color:var(--white)}
.hero-copy h1{font-size:44px;font-weight:600;line-height:1.3}
.hero .btn{position:absolute;left:84px;top:366px;border-color:var(--white);color:var(--white);font-size:24px;padding:12px 16px}
.hero-dots{position:absolute;left:570px;top:562px;display:flex;gap:12px}
.hero-dots span{width:16px;height:16px;border-radius:50%;border:2px solid var(--white)}
.hero-dots span.active{background:var(--white)}

.about{position:absolute;top:700px;left:0;width:1200px;height:320px;padding:36px 84px}
.about p{font-size:21px;line-height:1.75;margin:18px 0 26px}

.deals{position:absolute;top:1020px;left:0;width:1200px;height:610px;display:flex}
.deal{width:600px;height:100%;padding:44px 84px}
.deal:first-child{background:var(--peach)}
.deal:last-child{background:var(--sand);padding-left:76px}
.deal .section-title{font-size:26px}
.deal-photo{width:456px;height:300px;margin:28px 0 30px}
.deal p{font-size:19px;line-height:1.5;width:440px}
.deal .btn{margin-top:30px;font-size:20px;padding:6px 22px}

.gallery{position:absolute;top:1630px;left:0;width:1200px;height:420px;padding:42px 84px}
.gallery-grid{display:flex;gap:26px;margin-top:30px}
.gallery-grid div{width:326px;height:262px}

.contact{position:absolute;top:2050px;left:0;width:1200px;height:730px;background:var(--blush);padding:44px 84px}
.contact .section-title{font-size:36px}
.field-row{display:flex;gap:56px;margin-top:30px}
.field label,.message label{display:block;font-size:22px;font-weight:600;color:var(--plum);margin-bottom:16px}
.field .input{width:488px;height:74px;border:2px solid var(--white)}
.message{margin-top:28px}
.message .input{width:1032px;height:238px;border:2px solid var(--white)}
.contact .btn{position:absolute;left:84px;top:628px;font-size:22px;padding:8px 14px}

.site-footer{position:absolute;top:2780px;left:0;width:1200px;height:64px;background:var(--footer);color:#d8d8d8;font-size:17px;display:flex;align-items:center;justify-content:center}
</style>
</head>
<body>
<header class="site-header">
  <div class="brand"><span class="brand-dot"></span>Serene Beauty</div>
  <nav class="main-nav"><span>HOME</span><span>ABOUT</span><span>LATEST DEALS</span><span>TREATMENTS</span><span>PRODUCTS</span><span>CONTACT</span></nav>
</header>

<section class="hero">
  <div class="hero-photo" role="img" aria-label="Banner photo of a model applying lipstick against a rose-toned backdrop"></div>
  <div class="hero-copy"><h1>SERENE BEAUTY : A unique<br>solution for facials, massage,<br>medical treatments.</h1></div>
  <span class="btn">CONTACT NOW</span>
  <div class="hero-dots"><span class="active"></span><span></span><span></span></div>
</section>

<section class="about">
  <h2 class="section-title">ABOUT US</h2>
  <p>Lorem Ipsum is simply dummy text of the printing and typesetting industry. Lorem Ipsum has been the industry's standard dummy text ever since the 1500s, when an unknown printer took a galley of type and scrambled it to make a type specimen book.</p>
  <span class="btn">KNOW MORE</span>
</section>

<section class="deals">
  <article class="deal">
    <h2 class="section-title">LATEST DEALS</h2>
    <div class="deal-photo" role="img" aria-label="Photo of a facial injection treatment" style="background:linear-gradient(120deg,#e9d3c7,#f3e1d8 50%,#8fc6e6)"></div>
    <p>Lorem Ipsum is simply dummy text of the printing and typesetting industry.</p>
    <span class="btn">$56.10</span>
  </article>
  <article class="deal">
    <h2 class="section-title">LATEST DEALS</h2>
    <div class="deal-photo" role="img" aria-label="Photo of a hair and scalp treatment" style="background:linear-gradient(120deg,#6b5a4a,#c6b3a1 55%,#7b6f62)"></div>
    <p>Lorem Ipsum is simply dummy text of the printing and typesetting industry.</p>
    <span class="btn">$56.10</span>
  </article>
</section>

<section class="gallery">
  <h2 class="section-title">OUR GALLERY</h2>
  <div class="gallery-grid">
    <div role="img" aria-label="Salon treatment room with a massage bed" style="background:linear-gradient(160deg,#8a6e55,#c9a985 60%,#5c4735)"></div>
    <div role="img" aria-label="Salon lounge with sofa and warm lighting" style="background:linear-gradient(160deg,#a88c6c,#d9c3a1 55%,#6e5a46)"></div>
    <div role="img" aria-label="Client relaxing during a back massage with oil" style="background:linear-gradient(160deg,#e6cdb7,#c8906b 55%,#6a4a37)"></div>
  </div>
</section>

<section class="contact">
  <h2 class="section-title">GET IN TOUCH</h2>
  <div class="field-row">
    <div class="field"><label>NAME</label><div class="input"></div></div>
    <div class="field"><label>EMAIL</label><div class="input"></div></div>
  </div>
  <div class="message"><label>MESSAGE</label><div class="input"></div></div>
  <span class="btn">SEND MESSAGE</span>
</section>

<footer class="site-footer">@2018. All Rights Reserved</footer>
</body>
</html>
```